Post Lockdown Ortho Special

We are running a special for (Ortho) Braces/Clear Aligner (Quorventa), till July 31st 2020. Up to $2,000 off with free Consultation and Xrays.

We need a ad to run in different formats.

Maybe something with: what better time to get braces when you have to wear a mask all the time.

Trying to rebuild our business and get people in for free consultations.

```html
<!DOCTYPE html>
<html lang="en">
<head>
<meta charset="utf-8">
<title>Post Lockdown Ortho Special – Aspenridge Family Dentistry</title>
<link rel="stylesheet" href="https://fonts.googleapis.com/css2?family=Montserrat:wght@300;400;500;600;700;800;900&display=swap">
<style>
  :root {
    --purple: #673d9f;
    --purple-soft: #7a55ad;
    --ink: #0b0b0b;
    --white: #ffffff;
    --photo-light: #cbbbe4;
    --photo-mid: #a58fcf;
    --photo-deep: #8a6fc0;
  }
  * { margin: 0; padding: 0; box-sizing: border-box; }
  html, body { width: 1200px; height: 1080px; overflow: hidden; background: var(--white); }
  body { font-family: "Montserrat", sans-serif; }

  .ad {
    position: relative;
    width: 1200px;
    height: 1080px;
    overflow: hidden;
    background: var(--white);
  }

  .hero-art {
    position: absolute;
    left: 0; top: 0;
    width: 1200px; height: 1080px;
  }

  .brand {
    position: absolute;
    left: 56px; top: 66px;
    display: flex;
    align-items: center;
    gap: 16px;
    color: var(--purple);
    font-weight: 600;
  }
  .brand-dot {
    width: 96px; height: 96px;
    border-radius: 50%;
    background: var(--purple);
  }
  .brand-name { line-height: 1.15; }
  .brand-name .line-main { display: block; font-size: 30px; letter-spacing: 1px; }
  .brand-name .line-sub { display: block; font-size: 12px; letter-spacing: 5px; }
  .brand-name .line-doc { display: block; font-size: 11px; letter-spacing: 1.5px; margin-top: 6px; }

  .headline { position: absolute; left: 48px; top: 228px; line-height: 1; }
  .headline span { display: block; }
  .headline .post { font-weight: 300; font-size: 94px; color: var(--ink); letter-spacing: 1px; }
  .headline .lockdown { font-weight: 900; font-size: 101px; color: var(--ink); margin-top: 5px; letter-spacing: -1px; }
  .headline .ortho { font-weight: 800; font-size: 96px; color: var(--purple); margin-top: 6px; }
  .headline .special { font-weight: 300; font-size: 101px; color: var(--purple); margin-top: 0; }

  .divider {
    position: absolute;
    left: 52px; top: 669px;
    width: 210px; height: 6px;
    background: var(--purple);
  }

  .pitch { position: absolute; left: 56px; top: 716px; }
  .pitch .lead, .pitch .tail { font-weight: 400; font-size: 31px; color: var(--ink); letter-spacing: 0.5px; }
  .pitch .braces {
    font-weight: 800; font-size: 146px; color: var(--purple);
    line-height: 1; margin: 6px 0 0 -4px; letter-spacing: -2px;
  }
  .pitch .tail { margin-top: 4px; }

  .date-badge {
    position: absolute;
    left: 466px; top: 514px;
    width: 200px; height: 200px;
    border-radius: 50%;
    background: var(--purple);
    border: 9px solid var(--white);
    box-shadow: 0 0 0 1px rgba(0,0,0,0.04);
    color: var(--white);
    text-align: center;
    font-weight: 700;
    padding-top: 44px;
    line-height: 1;
  }
  .date-badge .till { font-size: 22px; text-align: left; padding-left: 30px; }
  .date-badge .day { font-size: 54px; font-weight: 800; margin-top: 0; }
  .date-badge .month { font-size: 22px; font-weight: 600; margin-top: 6px; }

  .offer-band {
    position: absolute;
    left: 0; top: 944px;
    width: 1200px; height: 94px;
  }
  .offer-text {
    position: absolute;
    left: 110px; top: 944px;
    height: 94px;
    display: flex;
    align-items: center;
    gap: 8px;
    color: var(--white);
    font-weight: 700;
    font-size: 31px;
    white-space: nowrap;
  }
  .offer-text .amount { font-size: 68px; font-weight: 800; letter-spacing: -1px; }

  .tooth-mark {
    position: absolute;
    left: 1062px; top: 930px;
    width: 106px; height: 130px;
    background: var(--white);
  }
</style>
</head>
<body>
  <main class="ad">
    <svg class="hero-art" viewBox="0 0 1200 1080" aria-hidden="false">
      <defs>
        <linearGradient id="photoTone" x1="0" y1="0" x2="1" y2="1">
          <stop offset="0" stop-color="var(--photo-deep)"/>
          <stop offset="0.45" stop-color="var(--photo-mid)"/>
          <stop offset="1" stop-color="var(--photo-light)"/>
        </linearGradient>
        <clipPath id="canvasClip"><rect width="1200" height="1080"/></clipPath>
      </defs>
      <g clip-path="url(#canvasClip)">
        <circle class="hero-ring" cx="905" cy="300" r="472" fill="var(--purple)"/>
        <circle class="hero-ring-gap" cx="915" cy="280" r="455" fill="var(--white)"/>
        <circle class="hero-photo" cx="925" cy="262" r="450" fill="url(#photoTone)"
                role="img" aria-label="Photo of a dentist in mask and cap treating a smiling young woman in the dental chair"/>
      </g>
    </svg>

    <div class="brand">
      <span class="brand-dot"></span>
      <span class="brand-name">
        <span class="line-main">ASPENRIDGE</span>
        <span class="line-sub">FAMILY DENTISTRY</span>
        <span class="line-doc">DR MIRIAM ELLERY</span>
      </span>
    </div>

    <h1 class="headline">
      <span class="post">POST</span>
      <span class="lockdown">LOCKDOWN</span>
      <span class="ortho">Ortho</span>
      <span class="special">Special</span>
    </h1>

    <div class="divider"></div>

    <div class="date-badge">
      <div class="till">Till</div>
      <div class="day">31st</div>
      <div class="month">July 2020</div>
    </div>

    <section class="pitch">
      <p class="lead">what better time to get</p>
      <p class="braces">BRACES</p>
      <p class="tail">when you have to wear a mask</p>
    </section>

    <svg class="offer-band" viewBox="0 0 1200 94" aria-hidden="true">
      <polygon points="46,94 110,0 1090,0 1090,94" fill="var(--purple)"/>
    </svg>
    <p class="offer-text">
      <span>Upto</span><span class="amount">$2,000</span><span>Off with free Consultation &amp; Xrays.</span>
    </p>

    <div class="tooth-mark" role="img" aria-label="Tooth outline icon"></div>
  </main>
</body>
</html>
```